Brolvane Tours - Astronomy in the Kimberley

Brolvane Tours requires a web page to advertise astronomy tours in the East Kimberley, Australia. It needs the following tabs - Home, Tours, Astronomy Events, Gallery, Testimonials, Contacts.

It should target tourists to the Kimberley.
We are unsure of which colours to go with at the moment but we have included our logo if it helps.

It should be mobile and tablet friendly.

Target Market(s)

Families, +40, Tourist, hobby astronomists,

Industry/Entity Type

Events

Number of Pages Required

3 page

Colors
3377b5
ffffff

Requirements
Must have
• Home, Tours, Astronomy Events, Gallery, Calendar, Testimonials, Contacts.
• 'Brolvane Tours' logo
Nice to have
• Pictures of portable amateur telescopes. Pictures of Lake Kununurra or Wyndham.
Should not have
• Pictures of extremely large professional telescopes.

```html
<!DOCTYPE html>
<html lang="en">
<head>
<meta charset="utf-8">
<title>Brolvane Tours – Astronomy in the Kimberley</title>
<link href="https://fonts.googleapis.com/css2?family=Open+Sans:wght@400;600;700&family=Arimo:wght@400;700&display=swap" rel="stylesheet">
<style>
  :root {
    --brand: #3a6cb5;
    --brand-dark: #2c5797;
    --footer: #3d6fb6;
    --ink: #444;
    --ink-soft: #666;
    --muted: #999;
    --page-grey: #f3f3f3;
    --white: #fff;
    --caption-dark: rgba(40,40,40,.85);
    --caption-blue: rgba(58,108,181,.88);
  }
  * { box-sizing: border-box; margin: 0; padding: 0; }
  html, body { width: 732px; height: 1200px; overflow: hidden; }
  body { font-family: "Open Sans", sans-serif; color: var(--ink); background: var(--white); }
  .page { position: relative; width: 732px; height: 1200px; background: linear-gradient(var(--white) 0 232px, var(--page-grey) 232px); }
  .abs { position: absolute; }

  /* header */
  .brand { left: 36px; top: 24px; display: flex; align-items: center; gap: 7px; font-size: 17px; font-weight: 600; color: var(--brand); }
  .brand-dot { width: 14px; height: 14px; border-radius: 50%; background: var(--brand); }
  .social-top { left: 441px; top: 24px; display: flex; gap: 13px; }
  .social-top span { width: 10px; height: 10px; border-radius: 50%; border: 1.3px solid #aaa; }
  .search { left: 535px; top: 21px; width: 160px; height: 18px; border: 1px solid #ccc; display: flex; }
  .search-field { flex: 1; font-size: 7px; color: #888; padding: 4px 6px; }
  .search-btn { width: 22px; background: var(--brand); display: flex; align-items: center; justify-content: center; }
  .nav-item { top: 58px; font-size: 9px; line-height: 12px; color: var(--ink); white-space: nowrap; text-decoration: none; }
  .nav-item.active { color: var(--brand); display: flex; align-items: center; gap: 6px; }

  /* hero */
  .hero-shadow { left: 22px; top: 100px; width: 688px; height: 296px; background: radial-gradient(ellipse at center, rgba(0,0,0,.22), transparent 70%); filter: blur(6px); }
  .hero { left: 37px; top: 90px; width: 658px; height: 306px; background: linear-gradient(135deg, #93a673, #5f8a7a 50%, #8ea36c); }
  .cap-title { left: 58px; top: 321px; padding: 3px 12px; background: var(--caption-dark); color: var(--white); font-size: 12px; }
  .cap-text { left: 58px; top: 349px; padding: 3px 12px; background: var(--caption-blue); color: var(--white); font-size: 12px; }
  .hero-arrow { top: 374px; width: 19px; height: 18px; display: flex; align-items: center; justify-content: center; }
  .hero-arrow.prev { left: 653px; background: #333; }
  .hero-arrow.next { left: 673px; background: var(--brand); }

  /* sections */
  .section-title { font-size: 13.5px; font-weight: 400; color: var(--ink); display: flex; align-items: center; gap: 7px; white-space: nowrap; }
  .welcome-text { left: 37px; top: 458px; width: 355px; font-size: 7.6px; line-height: 11.1px; color: var(--ink-soft); }
  .btn { background: var(--brand); color: var(--white); font-size: 8.5px; font-weight: 600; display: flex; align-items: center; justify-content: center; }
  .feature { top: 438px; width: 137px; }
  .feature-img { height: 90px; }
  .feature-label { margin-top: 6px; text-align: center; font-size: 10px; color: var(--ink); }

  .gallery-panel { left: 37px; top: 571px; width: 658px; height: 157px; background: var(--white); }
  .gallery-item { top: 613px; width: 148px; height: 99px; }
  .gallery-feature { background: var(--brand); color: var(--white); padding: 12px 14px; }
  .gallery-feature h3 { font-weight: 400; font-size: 13px; margin-bottom: 5px; }
  .gallery-feature p { font-size: 7.5px; line-height: 10px; opacity: .9; }

  .faces-strip { left: 37px; top: 786px; width: 658px; height: 44px; background: #d9d9d9; }
  .face { top: 786px; width: 45px; height: 44px; }
  .face-active-bar { left: 252px; top: 830px; width: 45px; height: 3px; background: #333; }
  .quote-arrow { top: 870px; width: 21px; height: 21px; border: 1px solid #e4e4e4; display: flex; align-items: center; justify-content: center; background: var(--white); }
  .quote-mark { left: 100px; top: 852px; font-family: Georgia, serif; font-size: 56px; color: #bbb; line-height: 1; }
  .quote-text { left: 143px; top: 869px; width: 520px; font-size: 10px; line-height: 18px; color: var(--ink-soft); }
  .quote-rule { left: 143px; top: 887px; width: 513px; height: 1px; background: #ddd; }
  .quote-dots { left: 352px; top: 926px; display: flex; gap: 3px; }
  .quote-dots span { width: 3px; height: 3px; border-radius: 50%; background: var(--brand); }
  .author { left: 0; width: 732px; text-align: center; font-family: "Arimo", sans-serif; }
  .author-name { top: 936px; font-size: 8.5px; font-weight: 700; color: #333; }
  .author-role { top: 949px; font-size: 7px; color: var(--muted); }

  /* footer */
  .footer { left: 0; top: 1004px; width: 732px; height: 162px; background: var(--footer); }
  .footer-heading { font-size: 8px; font-weight: 600; text-transform: uppercase; top: 1029px; color: var(--white); }
  .links { left: 38px; top: 1047px; list-style: none; font-size: 7.2px; line-height: 13px; color: var(--white); }
  .links li::before { content: ""; display: inline-block; width: 3.5px; height: 3.5px; border-radius: 50%; background: rgba(255,255,255,.45); margin-right: 9px; vertical-align: middle; }
  .event-thumb { width: 61px; height: 39px; }
  .footer-note { font-size: 7.2px; line-height: 9.6px; color: rgba(255,255,255,.7); }
  .contact-line { left: 365px; font-size: 7.2px; color: rgba(255,255,255,.7); display: flex; align-items: center; gap: 7px; }
  .field { left: 564px; width: 130px; height: 17px; background: rgba(255,255,255,.18); font-size: 7px; color: var(--white); padding: 4px 6px; display: flex; justify-content: space-between; align-items: center; }
  .contact-btn { left: 643px; top: 1130px; width: 50px; height: 14px; background: #213f6f; font-size: 7px; }
  .bottom-bar { left: 0; top: 1166px; width: 732px; height: 34px; background: var(--brand-dark); }
  .social-bottom { left: 38px; top: 1178px; display: flex; gap: 9px; }
  .social-bottom span { width: 10px; height: 10px; border-radius: 50%; background: var(--white); }
  .copyright { right: 37px; top: 1178px; font-size: 7px; color: var(--white); }
</style>
</head>
<body>
<div class="page">

  <!-- header -->
  <div class="abs brand"><span class="brand-dot"></span>Brolvane Tours</div>
  <div class="abs social-top"><span></span><span></span><span></span><span></span></div>
  <div class="abs search">
    <div class="search-field">Search Here</div>
    <div class="search-btn">
      <svg width="8" height="8" viewBox="0 0 10 10"><circle cx="4" cy="4" r="3" fill="none" stroke="#fff" stroke-width="1.4"/><line x1="6.2" y1="6.2" x2="9" y2="9" stroke="#fff" stroke-width="1.4"/></svg>
    </div>
  </div>
  <nav>
    <a class="abs nav-item active" style="left:253px">
      <svg width="11" height="11" viewBox="0 0 10 10"><path d="M5 0 L6 4 L10 5 L6 6 L5 10 L4 6 L0 5 L4 4 Z" fill="#3a6cb5"/></svg>Home</a>
    <a class="abs nav-item" style="left:333px">Tours</a>
    <a class="abs nav-item" style="left:393px">Astronomy Events</a>
    <a class="abs nav-item" style="left:505px">Gallery</a>
    <a class="abs nav-item" style="left:571px">Testimonials</a>
    <a class="abs nav-item" style="left:660px">Contacts</a>
  </nav>

  <!-- hero -->
  <div class="abs hero-shadow"></div>
  <div class="abs hero" role="img" aria-label="Aerial photo of a deep lake in the outback scrub"></div>
  <div class="abs cap-title">Congue id, luctus eu</div>
  <div class="abs cap-text">In nisi tellus, convallis sed congue id, luctus eu purus.</div>
  <div class="abs hero-arrow prev"><svg width="6" height="9" viewBox="0 0 6 9"><path d="M5 1 L1 4.5 L5 8" fill="none" stroke="#fff" stroke-width="1.3"/></svg></div>
  <div class="abs hero-arrow next"><svg width="6" height="9" viewBox="0 0 6 9"><path d="M1 1 L5 4.5 L1 8" fill="none" stroke="#fff" stroke-width="1.3"/></svg></div>

  <!-- welcome -->
  <h2 class="abs section-title" style="left:33px;top:434px">
    <svg width="11" height="11" viewBox="0 0 10 10"><path d="M5 0 L6 4 L10 5 L6 6 L5 10 L4 6 L0 5 L4 4 Z" fill="#3a6cb5"/></svg>Welcome To Our Site</h2>
  <p class="abs welcome-text">Proin massa nulla, dignissim ut efficitur at, viverra in quam. Donec condimentum nunc et dui egestas tristique. Fusce id nisl at mi lobortis eleifend sodales id mi. Mauris sed magna tortor. Phasellus a orci hendrerit, tempus ante rutrum, molestie lacus. Pellentesque finibus dictum est sed pharetra. Donec finibus lorem nec felis ullamcorper suscipit. Suspendisse sagittis, purus nec venenatis facilisis, mi ante ultrices magna, et ornare nunc mauris eget metus.</p>
  <div class="abs btn" style="left:37px;top:523px;width:76px;height:18px">Read More</div>

  <div class="abs feature" style="left:406px">
    <div class="feature-img" role="img" aria-label="Photo of caravan trailers on a lawn" style="background:linear-gradient(160deg,#6f8f52,#4a7a32)"></div>
    <div class="feature-label">Caravan Trailers</div>
  </div>
  <div class="abs feature" style="left:558px">
    <div class="feature-img" role="img" aria-label="Photo of an astronomy exhibition hall" style="background:linear-gradient(160deg,#5a6f90,#34476a)"></div>
    <div class="feature-label">Astronomy Tours</div>
  </div>

  <!-- gallery -->
  <div class="abs gallery-panel"></div>
  <h2 class="abs section-title" style="left:316px;top:581px">
    <svg width="11" height="11" viewBox="0 0 10 10"><path d="M5 0 L6 4 L10 5 L6 6 L5 10 L4 6 L0 5 L4 4 Z" fill="#3a6cb5"/></svg>Our Gallery</h2>
  <div class="abs gallery-item" style="left:47px;background:linear-gradient(160deg,#7c8aa3,#6a5a4e)" role="img" aria-label="Photo of a historic town square"></div>
  <div class="abs gallery-item gallery-feature" style="left:210px">
    <h3>Kimberley</h3>
    <p>Lorem ipsum dolor sit amet, con-<br>sectetur adipiscing elit.</p>
    <svg width="16" height="16" viewBox="0 0 16 16" style="margin-top:8px"><circle cx="8" cy="8" r="7" fill="none" stroke="#fff" stroke-width="1.2"/><path d="M8 4.5v7M4.5 8h7" stroke="#fff" stroke-width="1.2"/></svg>
    <svg width="15" height="15" viewBox="0 0 15 15" style="position:absolute;right:0;bottom:0"><path d="M15 0 V15 H0 Z" fill="#2c5797"/></svg>
  </div>
  <div class="abs gallery-item" style="left:374px;background:linear-gradient(160deg,#1d222b,#4a4232)" role="img" aria-label="Photo of a lit church tower at night"></div>
  <div class="abs gallery-item" style="left:537px;background:linear-gradient(160deg,#7a5a52,#5a6478)" role="img" aria-label="Photo of a river gorge under blue sky"></div>

  <!-- testimonials -->
  <h2 class="abs section-title" style="left:309px;top:756px">
    <svg width="11" height="11" viewBox="0 0 10 10"><path d="M5 0 L6 4 L10 5 L6 6 L5 10 L4 6 L0 5 L4 4 Z" fill="#3a6cb5"/></svg>Testimonials</h2>
  <div class="abs faces-strip"></div>
  <div class="abs face" style="left:252px;background:#a86a52" role="img" aria-label="Reviewer portrait"></div>
  <div class="abs face" style="left:297px;background:#d4c2b0" role="img" aria-label="Reviewer portrait"></div>
  <div class="abs face" style="left:342px;background:#bcb6b0" role="img" aria-label="Reviewer portrait"></div>
  <div class="abs face" style="left:387px;background:#e0cc98" role="img" aria-label="Reviewer portrait"></div>
  <div class="abs face" style="left:432px;background:#c47e98" role="img" aria-label="Reviewer portrait"></div>
  <div class="abs face-active-bar"></div>

  <div class="abs quote-arrow" style="left:37px"><svg width="5" height="8" viewBox="0 0 5 8"><path d="M4 1 L1 4 L4 7" fill="none" stroke="#999"/></svg></div>
  <div class="abs quote-arrow" style="left:674px"><svg width="5" height="8" viewBox="0 0 5 8"><path d="M1 1 L4 4 L1 7" fill="none" stroke="#999"/></svg></div>
  <div class="abs quote-mark">&#8221;</div>
  <div class="abs quote-rule"></div>
  <p class="abs quote-text">Vitae adipiscing turpis. Aenean ligula nibh, molestie id viverra a, dapibus at dolor. In iaculis viverra neque, ac eleifend ante lobortis id. In viverra ipsum ...</p>
  <div class="abs quote-dots"><span></span><span></span><span></span></div>
  <div class="abs author author-name">Dorian Kessly</div>
  <div class="abs author author-role">General Director</div>

  <!-- footer -->
  <footer class="abs footer"></footer>
  <h4 class="abs footer-heading" style="left:38px">Useful Links</h4>
  <ul class="abs links">
    <li>Home</li><li>Tours</li><li>Astronomy Events</li><li>Gallery</li><li>Testimonials</li><li>Contacts</li>
  </ul>

  <h4 class="abs footer-heading" style="left:168px">Latest Events</h4>
  <div class="abs event-thumb" style="left:170px;top:1049px;background:linear-gradient(160deg,#8a93a6,#6a5e58)" role="img" aria-label="Event photo: town square"></div>
  <div class="abs event-thumb" style="left:232px;top:1049px;background:linear-gradient(160deg,#5e5e66,#7e7260)" role="img" aria-label="Event photo: old clock"></div>
  <div class="abs event-thumb" style="left:170px;top:1090px;background:linear-gradient(160deg,#1e3a3e,#2e6a56)" role="img" aria-label="Event photo: aurora night sky"></div>
  <div class="abs event-thumb" style="left:232px;top:1090px;background:linear-gradient(160deg,#2a2238,#6a3a3a)" role="img" aria-label="Event photo: night market"></div>

  <h4 class="abs footer-heading" style="left:363px">Get In Touch</h4>
  <p class="abs footer-note" style="left:364px;top:1047px;width:150px">Doloreiur quia commolu ptatemp dolupta oreprerum tibusam eumenis et consent accullignis dentibea</p>
  <div class="abs contact-line" style="top:1084px">
    <svg width="6" height="8" viewBox="0 0 6 8"><path d="M3 8 C1 5 0 4 0 3 A3 3 0 0 1 6 3 C6 4 5 5 3 8Z" fill="rgba(255,255,255,.8)"/></svg>12 Ord Street, Kununurra, WA 6743</div>
  <div class="abs contact-line" style="top:1097px">
    <svg width="7" height="7" viewBox="0 0 8 8"><path d="M1 0 L3 0 L3.5 2 L2.3 3 C3 4.5 3.5 5 5 5.7 L6 4.5 L8 5 L8 7 C8 7.6 7.6 8 7 8 C3 8 0 5 0 1 C0 .4 .4 0 1 0Z" fill="rgba(255,255,255,.8)"/></svg>(555) 21 - 740 - 1196</div>
  <div class="abs contact-line" style="top:1110px">
    <svg width="8" height="6" viewBox="0 0 8 6"><rect width="8" height="6" fill="rgba(255,255,255,.8)"/><path d="M0 0 L4 3.5 L8 0" fill="none" stroke="#3d6fb6" stroke-width=".8"/></svg>hello@brolvanetours.example</div>

  <h4 class="abs footer-heading" style="left:562px">Contact</h4>
  <p class="abs footer-note" style="left:563px;top:1047px;width:130px">Doloreiur quia commolu ptatemp dolupta oreprerum</p>
  <div class="abs field" style="top:1078px">Email</div>
  <div class="abs field" style="top:1101px">Contact For
    <svg width="7" height="4" viewBox="0 0 7 4"><path d="M.5 .5 L3.5 3.5 L6.5 .5" fill="none" stroke="#fff"/></svg></div>
  <div class="abs btn contact-btn">CONTACT</div>

  <div class="abs bottom-bar"></div>
  <div class="abs social-bottom"><span></span><span></span><span></span><span></span></div>
  <div class="abs copyright">© 2015 Brolvane Tours. All rights reserved.</div>
</div>
</body>
</html>
```